IT Distribution Wholesale Business Card & Logo Design

I need both logo and a business card that suits our business model, am happy to pay more for great effort put in.
Brevon Orbital Australia Pty Ltd
An IT Distribution / Wholesale company that distributes technology hardwares, softwares, components, etc.
Offer drop ship services for online retailers and supply to Australia-wide.
Based in Sydney Australia.
Design should give impressions of trust and stability.

Slogan: "your one stop technology supplier"
*two-sided name card
*logo + slogan on the back of the card

I don't have much specific requirements, leave it to designers to come up with creative & interesting masterpiece.
The logo and business card comes in first which i would like it to be completed latest by mid of March, we will require a whole redesign of our web pages, banner design, catalogue design later part.

Goodluck & thank you for your effort.

Hello designers,

Busy week, very good return rate on the number of designs and effort put into our business card design.
I thank you all for that.
We will have to extend this project for another week to two to receive more designs and more time for me to post some updates to you all.
We are getting there, i really liked some of the designs sent but just not the perfect masterpiece we are looking for.

Cheers,
Darnell Q.

Target Market(s)

Computer Retailers, Corporate, Schools, Councils.

Industry/Entity Type

Business

Requirements
Must have
• Brevon Orbital (Australia) Pty Ltd, Darnell Quist, Managing Director, Unit C, 14-18 Pellham Road, Dunmore NSW 2461, Ph +61 2 5037 1942, M +61 4 70395216, E darnell@brevonorbital.com.au, W www.brevonorbital.com.au
Nice to have
• Keep it simple & comfortable.
Target audiences are mostly >30-40 years old range.

Example of companies in the same line:-
http://www.kzp.com.au
http://www.norvix.com.au/
http://www.supplyhaventrade.com/
http://www.quenby.com.au/
http://www.bq456.com.au/
https://www.swiftgridhub.com.au/
http://carvelo.com.au/

```html
<!DOCTYPE html>
<html lang="en">
<head>
<meta charset="utf-8">
<title>Brevon Orbital Business Card</title>
<link rel="stylesheet" href="https://fonts.googleapis.com/css2?family=Arimo:wght@400;700&display=swap">
<style>
  :root {
    --stage: #d9dbde;
    --card: #ffffff;
    --navy: #1c2370;
    --sky: #2a8fd0;
    --ink: #3d3d3d;
    --rule: #2b3283;
    --mark: #2f4fb8;
  }
  * { margin: 0; padding: 0; box-sizing: border-box; }
  html, body { width: 1200px; height: 861px; overflow: hidden; }
  body {
    background: var(--stage);
    font-family: "Arimo", Arial, sans-serif;
    display: flex;
    align-items: center;
    justify-content: center;
    gap: 36px;
  }
  .card {
    width: 540px;
    height: 330px;
    background: var(--card);
    box-shadow: 0 6px 18px rgba(0,0,0,0.18);
    display: flex;
    flex-direction: column;
    align-items: center;
  }
  .brand { display: flex; flex-direction: column; align-items: center; }
  .brand-dot { display: block; }
  .brand-name {
    font-weight: 700;
    color: var(--ink);
    font-size: 17px;
    margin-top: 8px;
  }
  .card-front { padding-top: 34px; }
  .person { text-align: center; margin-top: 20px; }
  .person-name { color: var(--navy); font-weight: 700; font-size: 27px; }
  .person-role { color: var(--ink); font-size: 16px; margin-top: 2px; }
  .rule { width: 390px; height: 2px; background: var(--rule); margin: 12px 0 10px; }
  .contact { list-style: none; text-align: center; font-size: 14.5px; line-height: 20px; color: var(--ink); }
  .contact .label { color: var(--sky); font-weight: 700; margin-right: 4px; }
  .card-back { padding-top: 68px; }
  .card-back .brand-name { font-size: 21px; margin-top: 12px; }
  .card-back .rule { width: 400px; margin: 22px 0 8px; }
  .slogan { color: var(--sky); font-weight: 700; font-size: 23px; }
</style>
</head>
<body>
  <section class="card card-front">
    <div class="brand">
      <svg class="brand-dot" width="56" height="56" viewBox="0 0 56 56" aria-hidden="true"><circle cx="28" cy="28" r="26" fill="var(--mark)"/></svg>
      <p class="brand-name">Brevon Orbital (Australia) Pty Ltd</p>
    </div>
    <div class="person">
      <h1 class="person-name">Darnell Quist</h1>
      <p class="person-role">Managing Director</p>
    </div>
    <div class="rule"></div>
    <ul class="contact">
      <li><span class="label">Address</span>Unit C, 14-18 Pellham Road, Dunmore NSW 2461</li>
      <li><span class="label">Phone</span>+61 2 5037 1942</li>
      <li><span class="label">Mobile</span>+61 4 70395216</li>
      <li><span class="label">E-mail</span>darnell@brevonorbital.com.au</li>
      <li><span class="label">Website</span>www.brevonorbital.com.au</li>
    </ul>
  </section>
  <section class="card card-back">
    <div class="brand">
      <svg class="brand-dot" width="72" height="72" viewBox="0 0 72 72" aria-hidden="true"><circle cx="36" cy="36" r="34" fill="var(--mark)"/></svg>
      <p class="brand-name">Brevon Orbital (Australia) Pty Ltd</p>
    </div>
    <div class="rule"></div>
    <p class="slogan">Your one stop technology supplier.</p>
  </section>
</body>
</html>
```